Need a webinar banner promo to place on social media

We are organise a series of webinars in coming months.

We need a webinar banner design to be posted on Facebook and linkedin. The banner is for our webinar titled: Steps to Unveil your venture with poise and polish.

our website is www.bravolinhub.com.au

there is a link on the website to the webinar registration for your reference.

```html
<!DOCTYPE html>
<html lang="en">
<head>
<meta charset="utf-8">
<title>Bravolin Hub – Free Webinar Banners</title>
<link rel="stylesheet" href="https://fonts.googleapis.com/css2?family=Montserrat:wght@700;800&family=Barlow+Semi+Condensed:wght@300;400&family=Roboto:wght@400&display=swap">
<style>
  :root {
    --page: #ffffff;
    --cream: #f8f0cf;
    --cream-light: #fdf9e8;
    --navy: #0b2140;
    --band: #1e2a3c;
    --gold: #b5862f;
    --gold-light: #d9b24a;
    --gold-pale: #ecd27a;
    --ink: #0b2140;
    --text: #1a1a1a;
    --photo-warm: #b8322a;
    --photo-dark: #2a2e3a;
  }
  * { margin: 0; padding: 0; box-sizing: border-box; }
  html, body {
    width: 1200px; height: 585px; overflow: hidden;
    background: var(--page);
  }
  .canvas { position: relative; width: 1200px; height: 585px; }
  .banner { position: absolute; top: 81px; height: 426px; display: block; }
  .banner--wide { left: 42px; width: 640px; }
  .banner--square { left: 730px; width: 427px; }

  .bg-cream { fill: url(#creamGlow); }
  .shape-navy { fill: var(--navy); }
  .shape-gold { fill: var(--gold); }
  .shape-gold-light { fill: var(--gold-pale); }
  .band { fill: var(--band); }
  .ring { fill: url(#goldRing); }
  .photo { fill: url(#photoTone); }

  .badge-icon { fill: var(--cream-light); stroke: var(--gold); }
  .badge-play { fill: var(--gold); }
  .badge-live { fill: var(--gold); font-family: 'Montserrat', sans-serif; font-weight: 800; }
  .badge-box { fill: var(--navy); }
  .badge-text { fill: #ffffff; font-family: 'Roboto', sans-serif; font-weight: 400; }

  .title { fill: var(--ink); font-family: 'Montserrat', sans-serif; font-weight: 800; }
  .datetime { fill: var(--text); font-family: 'Barlow Semi Condensed', sans-serif; font-weight: 300; }
  .body-copy { fill: var(--text); font-family: 'Barlow Semi Condensed', sans-serif; font-weight: 400; }
  .register { fill: var(--ink); font-family: 'Barlow Semi Condensed', sans-serif; font-weight: 400; }
  .web-address { fill: var(--text); font-family: 'Barlow Semi Condensed', sans-serif; font-weight: 400; }
  .brand-name { fill: var(--gold-light); font-family: 'Montserrat', sans-serif; font-weight: 800; }
</style>
</head>
<body>
<div class="canvas">

  <svg width="0" height="0" aria-hidden="true" style="position:absolute">
    <defs>
      <radialGradient id="creamGlow" cx="0.3" cy="0.4" r="0.9">
        <stop offset="0" stop-color="#fdf9e8"/>
        <stop offset="1" stop-color="#f5ebc4"/>
      </radialGradient>
      <linearGradient id="goldRing" x1="0" y1="0" x2="1" y2="1">
        <stop offset="0" stop-color="#b8892c"/>
        <stop offset="0.45" stop-color="#ecd27a"/>
        <stop offset="1" stop-color="#a87a25"/>
      </linearGradient>
      <linearGradient id="photoTone" x1="0" y1="0" x2="0" y2="1">
        <stop offset="0" stop-color="#2c3b6e"/>
        <stop offset="0.45" stop-color="#b8322a"/>
        <stop offset="0.75" stop-color="#d9c8c0"/>
        <stop offset="1" stop-color="#1c1c22"/>
      </linearGradient>
    </defs>
  </svg>

  <!-- Wide banner -->
  <svg class="banner banner--wide" viewBox="0 0 1365 909" role="group" aria-label="Free webinar banner, wide format">
    <rect class="bg-cream" width="1365" height="909"/>
    <polygon class="shape-navy" points="1123,0 1365,0 1365,909 1230,909 628,599 765,584"/>
    <polygon class="shape-gold-light" points="628,599 765,584 728,652"/>
    <polygon class="shape-gold" points="628,599 1230,909 482,909"/>
    <rect class="band" x="0" y="742" width="620" height="46"/>

    <circle class="ring" cx="972" cy="409" r="233"/>
    <circle class="photo" cx="972" cy="409" r="212" role="img" aria-label="Group photo of authors holding their books at a launch event"/>

    <text class="brand-name" x="1213" y="128" font-size="44" text-anchor="middle">BRAVOLIN</text>
    <text class="brand-name" x="1213" y="168" font-size="44" text-anchor="middle">HUB</text>

    <g class="badge">
      <rect class="badge-box" x="230" y="41" width="314" height="52"/>
      <rect x="73" y="41" width="170" height="52" rx="26" fill="var(--cream-light)" stroke="var(--gold)" stroke-width="5"/>
      <circle class="badge-icon" cx="99" cy="67" r="22" stroke-width="5"/>
      <polygon class="badge-play" points="92,55 92,79 111,67"/>
      <text class="badge-live" x="133" y="84" font-size="40">LIVE</text>
      <text class="badge-text" x="253" y="83" font-size="37">FREE WEBINAR</text>
    </g>

    <text class="title" font-size="58">
      <tspan x="73" y="192">STEPS TO UNVEIL</tspan>
      <tspan x="73" y="260">YOUR VENTURE</tspan>
      <tspan x="73" y="327">WITH POISE</tspan>
      <tspan x="73" y="395">AND POLISH</tspan>
    </text>

    <text class="datetime" font-size="54">
      <tspan x="72" y="479">MARCH 15, 2023</tspan>
      <tspan x="72" y="544">7:00PM AEDT</tspan>
    </text>

    <text class="body-copy" font-size="21">
      <tspan x="73" y="584">Worried that the process of launching your book isn’t</tspan>
      <tspan x="73" y="610">glamorous enough?</tspan>
      <tspan x="73" y="654">Don’t Worry, this webinar has all the tips &amp; tricks</tspan>
      <tspan x="73" y="680">to help you glam up your book launch and make</tspan>
      <tspan x="73" y="705">it something people will remember.</tspan>
    </text>

    <text class="web-address" x="73" y="827" font-size="28">www.bravolinhub.com.au</text>
  </svg>

  <!-- Square banner -->
  <svg class="banner banner--square" viewBox="0 0 911 909" role="group" aria-label="Free webinar banner, square format">
    <rect class="bg-cream" width="911" height="909"/>
    <polygon class="shape-navy" points="690,0 911,0 911,909 432,579"/>
    <polygon class="shape-gold-light" points="432,579 472,577 455,604"/>
    <polygon class="shape-gold" points="432,579 911,909 267,909"/>
    <rect class="band" x="0" y="789" width="320" height="36"/>

    <circle class="ring" cx="617" cy="397" r="205"/>
    <circle class="photo" cx="617" cy="397" r="185" role="img" aria-label="Group photo of authors holding their books at a launch event"/>

    <text class="brand-name" x="787" y="100" font-size="44" text-anchor="middle">BRAVOLIN</text>
    <text class="brand-name" x="787" y="140" font-size="44" text-anchor="middle">HUB</text>

    <g class="badge">
      <rect class="badge-box" x="175" y="53" width="237" height="40"/>
      <rect x="49" y="53" width="136" height="40" rx="20" fill="var(--cream-light)" stroke="var(--gold)" stroke-width="4"/>
      <circle class="badge-icon" cx="69" cy="73" r="17" stroke-width="4"/>
      <polygon class="badge-play" points="64,64 64,82 78,73"/>
      <text class="badge-live" x="97" y="86" font-size="31">LIVE</text>
      <text class="badge-text" x="187" y="85" font-size="28">FREE WEBINAR</text>
    </g>

    <text class="title" font-size="44">
      <tspan x="50" y="172">STEPS TO UNVEIL</tspan>
      <tspan x="50" y="224">YOUR VENTURE</tspan>
      <tspan x="50" y="277">WITH POISE</tspan>
      <tspan x="50" y="329">AND POLISH</tspan>
    </text>

    <text class="datetime" font-size="43">
      <tspan x="43" y="407">MARCH 15, 2023</tspan>
      <tspan x="43" y="457">7:00PM AEDT</tspan>
    </text>

    <text class="body-copy" font-size="16.5">
      <tspan x="43" y="512">Worried that the process of launching your book isn’t</tspan>
      <tspan x="43" y="532">glamorous enough?</tspan>
      <tspan x="43" y="577">Don’t Worry, this webinar has all the tips &amp; tricks</tspan>
      <tspan x="43" y="597">to help you glam up your book launch and make</tspan>
      <tspan x="43" y="617">it something people will remember.</tspan>
    </text>

    <text class="register" x="43" y="715" font-size="31">REGISTER @</text>
    <text class="web-address" x="44" y="740" font-size="18.5">www.bravolinhub.com.au</text>
  </svg>

</div>
</body>
</html>
```